Full-Page Advertisement Design for IT Solutions & Online Store in English Magazine

We are seeking a fresh and creative full-page advertisement design for our IT solutions company, Bright Ledger, to be featured in an English-language magazine.
Ad Format: Full-page design for a print magazine.
Language: English.
Target Audience: Residents and holidaymakers, including those with holiday homes, seeking reliable IT services and products.
Main Title:
Text: "Exceptional IT Services and IT Support: Perfect for Residents and Holidaymakers"
Services List:
Smart Home Entertainment
Network & WiFi
Surveillance & Intercom Systems
Tech Support
Online Shop
Online Shop Promotion text:
"Explore our online shop with over 12,000 products, enjoy 2-day delivery, and benefit from tracking and dedicated customer support until your order arrives."

Contact Information:
Address: Quinta do Vale Morto Bloco 4C, loja 3, 8400-527 Lagoa
Opening Hours: Monday-Friday 9am-1pm and 3pm-7pm
Phone: 282 461 927
Online Store: loja.bright-ledger.example
Website: bright-ledger.example
Design Expectations:
The design should be clean, professional, and visually appealing, fully aligning with our brand identity.
The layout should be clear and easy to read, with the logo and key information immediately catching the eye.
The Logo should stand out in the page as its also represent our company name.
The main idea of this design is to introduce ourselves to the magazine and its readers, introduce we are. which will be followed by more design in the coming edition of the magazine.
Deliverables:
File Format: High-resolution PDF and source file (AI, PSD, etc.) suitable for print.
Revisions: We may request revisions to ensure the design fully meets our expectations before approval.
We are looking for a design that not only meets these specific requirements but also stands out visually and effectively communicates our services and brand values.
I have attached the logo file.
Thank you.

Target Market(s)

English Residents and holidaymakers, including those with holiday homes, seeking reliable IT services and products.

Industry/Entity Type

IT

Requirements
Must have
• Logo service list and address

```html
<!DOCTYPE html>
<html lang="en">
<head>
<meta charset="utf-8">
<title>Bright Ledger – Full-Page Advertisement</title>
<link rel="stylesheet" href="https://fonts.googleapis.com/css2?family=Roboto:wght@300;400;500;700;900&family=Roboto+Condensed:wght@500;700&display=swap">
<style>
  :root {
    --navy: #0e3a52;
    --navy-deep: #0a2e44;
    --green: #27b36a;
    --green-bright: #2fc777;
    --ink: #1c2a36;
    --paper: #ffffff;
    --stage: #eceef0;
    --tile: #e3e7ea;
  }
  * { margin: 0; padding: 0; box-sizing: border-box; }
  html, body { width: 1200px; height: 596px; overflow: hidden; background: var(--stage); }
  body { font-family: "Roboto", Arial, sans-serif; color: var(--ink); }

  .ad {
    position: absolute; left: 366px; top: 0;
    width: 468px; height: 596px;
    background: var(--paper); overflow: hidden;
  }
  .ad > * { position: absolute; }

  .backdrop { left: 0; top: 0; width: 468px; height: 596px; }

  /* Brand name */
  .brand { left: 32px; top: 34px; display: flex; align-items: center; gap: 10px; }
  .brand-square { width: 26px; height: 26px; background: var(--navy); }
  .brand-name {
    font-weight: 900; font-size: 27px; line-height: 29px;
    letter-spacing: 2px; color: var(--navy); text-transform: uppercase;
  }

  /* Headline band */
  .headline-band { left: 0; top: 106px; width: 390px; height: 151px; }
  .headline { left: 32px; top: 114px; color: #fff; }
  .headline-lead { font-weight: 300; font-size: 26px; line-height: 30px; }
  .headline-main { font-weight: 700; font-size: 37px; line-height: 35px; color: var(--green-bright); }
  .headline-and { font-weight: 400; font-size: 26px; color: #fff; }
  .headline-rule { left: 32px; top: 227px; width: 292px; height: 1px; background: rgba(255,255,255,.85); }
  .headline-sub { left: 32px; top: 230px; font-size: 15px; font-weight: 400; color: #fff; }

  /* Portrait area */
  .portrait { left: 0; top: 256px; width: 240px; height: 280px; }

  /* Services */
  .services-title {
    left: 212px; top: 264px;
    font-family: "Roboto Condensed", "Arial Narrow", sans-serif;
    font-weight: 500; font-size: 21px; color: var(--green);
  }
  .services-list { left: 213px; top: 289px; list-style: none; }
  .services-list li {
    display: flex; align-items: center; gap: 7px;
    height: 18.3px; font-size: 14px; color: var(--navy-deep);
  }
  .tick { width: 12px; height: 12px; flex: none; }

  .promo {
    left: 249px; top: 394px; width: 190px;
    border-left: 1.5px solid var(--green);
    padding-left: 7px; font-size: 8.2px; line-height: 12.8px; color: var(--ink);
  }

  /* Contact block */
  .contact-shape { left: 0; top: 470px; width: 468px; height: 113px; }
  .contact-title {
    left: 260px; top: 475px; font-size: 11.5px; color: var(--green-bright);
    border-bottom: 1px solid rgba(255,255,255,.5); padding-right: 8px; padding-bottom: 1px;
  }
  .contact-phone { left: 263px; top: 494px; display: flex; align-items: center; gap: 9px; color: #fff; font-weight: 700; font-size: 14px; }
  .icon { flex: none; }
  .hours { left: 263px; top: 517px; }
  .hours-row { display: flex; align-items: center; gap: 6px; }
  .hours-label { background: var(--green); color: #fff; font-weight: 700; font-size: 8px; padding: 1px 4px; }
  .hours-days { color: #fff; font-weight: 700; font-size: 9.5px; }
  .hours-times {
    margin-top: 2px; display: flex; align-items: center; gap: 4px;
    border: 1px solid var(--green); padding: 1px 4px; color: #fff; font-size: 9px;
  }
  .hours-times small { font-size: 6.5px; }
  .hours-times .and { color: var(--green-bright); }
  .address { left: 170px; top: 555px; display: flex; align-items: center; gap: 5px; color: #fff; font-size: 9.3px; }

  /* Online store */
  .store-label { left: 33px; top: 523px; background: var(--navy-deep); color: #fff; font-weight: 700; font-size: 10px; padding: 1px 4px; }
  .store-url {
    left: 34px; top: 538px; font-size: 10.5px; color: var(--green);
    border-bottom: 1px solid var(--green); padding-bottom: 1px;
  }
  .site-url { left: 34px; top: 555px; display: flex; align-items: center; gap: 4px; font-size: 9px; color: var(--green); }
</style>
</head>
<body>
<main class="ad">

  <svg class="backdrop" viewBox="0 0 468 596" aria-hidden="true">
    <g fill="var(--tile)" opacity=".55">
      <polygon points="350,0 468,0 468,60 410,120"/>
      <polygon points="300,60 370,130 300,200 230,130" opacity=".5"/>
      <polygon points="420,140 468,188 468,260 420,308 372,260" opacity=".6"/>
      <polygon points="330,360 390,420 330,480 270,420" opacity=".5"/>
      <polygon points="20,330 60,370 20,410 -20,370" opacity=".6"/>
      <polygon points="150,440 200,490 150,540 100,490" opacity=".5"/>
    </g>
  </svg>

  <div class="brand">
    <span class="brand-square"></span>
    <span class="brand-name">Bright<br>Ledger</span>
  </div>

  <svg class="headline-band" viewBox="0 0 390 151" aria-hidden="true">
    <defs>
      <linearGradient id="bandFill" x1="0" x2="1" y1="0" y2="0">
        <stop offset="0" stop-color="#1f9b5e"/>
        <stop offset=".28" stop-color="#0e3a52"/>
        <stop offset="1" stop-color="#0e3a52"/>
      </linearGradient>
    </defs>
    <polygon points="0,0 240,0 390,151 0,151" fill="url(#bandFill)"/>
  </svg>
  <h1 class="headline">
    <span class="headline-lead">Exceptional</span><br>
    <span class="headline-main">IT Services</span><br>
    <span class="headline-main"><span class="headline-and">and </span>IT Support:</span>
  </h1>
  <div class="headline-rule"></div>
  <p class="headline-sub">Perfect for Residents and Holidaymakers</p>

  <svg class="portrait" viewBox="0 0 240 280" role="img" aria-label="Photo of a smiling IT consultant in a blazer, arms crossed, framed by a green and navy diamond">
    <defs>
      <linearGradient id="diamondFill" x1="0" x2="1" y1="0" y2="1">
        <stop offset="0" stop-color="#2fc777"/>
        <stop offset=".55" stop-color="#14644f"/>
        <stop offset="1" stop-color="#0e3a52"/>
      </linearGradient>
      <linearGradient id="personFill" x1="0" x2="0" y1="0" y2="1">
        <stop offset="0" stop-color="#5b6670"/>
        <stop offset="1" stop-color="#26323c"/>
      </linearGradient>
    </defs>
    <polygon points="121,50 227,156 121,262 15,156" fill="url(#diamondFill)"/>
    <rect x="50" y="10" width="115" height="255" rx="40" fill="url(#personFill)" opacity=".55"/>
  </svg>

  <h2 class="services-title">Our Services</h2>
  <ul class="services-list">
    <li><svg class="tick" viewBox="0 0 12 12" aria-hidden="true"><polygon points="6,0 12,6 6,12 0,6" fill="var(--navy)"/><path d="M2.5 6.2 5 8.6 11 1.5" stroke="var(--green-bright)" stroke-width="2" fill="none"/></svg>Smart Home Entertainment</li>
    <li><svg class="tick" viewBox="0 0 12 12" aria-hidden="true"><polygon points="6,0 12,6 6,12 0,6" fill="var(--navy)"/><path d="M2.5 6.2 5 8.6 11 1.5" stroke="var(--green-bright)" stroke-width="2" fill="none"/></svg>Network &amp; WiFi</li>
    <li><svg class="tick" viewBox="0 0 12 12" aria-hidden="true"><polygon points="6,0 12,6 6,12 0,6" fill="var(--navy)"/><path d="M2.5 6.2 5 8.6 11 1.5" stroke="var(--green-bright)" stroke-width="2" fill="none"/></svg>Surveillance &amp; Intercom Systems</li>
    <li><svg class="tick" viewBox="0 0 12 12" aria-hidden="true"><polygon points="6,0 12,6 6,12 0,6" fill="var(--navy)"/><path d="M2.5 6.2 5 8.6 11 1.5" stroke="var(--green-bright)" stroke-width="2" fill="none"/></svg>Tech Support</li>
    <li><svg class="tick" viewBox="0 0 12 12" aria-hidden="true"><polygon points="6,0 12,6 6,12 0,6" fill="var(--navy)"/><path d="M2.5 6.2 5 8.6 11 1.5" stroke="var(--green-bright)" stroke-width="2" fill="none"/></svg>Online Shop</li>
  </ul>

  <p class="promo">Explore our online shop with<br>over 12,000 products,<br>enjoy 2-day delivery, and benefit from<br>tracking and dedicated customer support<br>until your order arrives.</p>

  <svg class="contact-shape" viewBox="0 0 468 113" aria-hidden="true">
    <polygon points="246,0 468,0 468,113 134,113" fill="var(--navy)"/>
    <polygon points="166,81 468,81 468,113 134,113" fill="var(--green)"/>
  </svg>
  <p class="contact-title">Contact Us Today</p>
  <p class="contact-phone">
    <svg class="icon" width="10" height="10" viewBox="0 0 10 10" aria-hidden="true"><rect width="10" height="10" rx="1" fill="var(--green-bright)"/><path d="M3 2.2c-.6.4-.8 1.2-.3 2.2.8 1.6 2 2.8 3.3 3.3.8.3 1.4 0 1.8-.5L6.7 6.1l-.8.5c-.7-.3-1.4-1-1.8-1.8l.5-.8z" fill="#fff"/></svg>
    282 461 927
  </p>
  <div class="hours">
    <div class="hours-row"><span class="hours-label">Opening Hours:</span><span class="hours-days">Monday - Friday</span></div>
    <div class="hours-times">
      <svg class="icon" width="8" height="8" viewBox="0 0 8 8" aria-hidden="true"><circle cx="4" cy="4" r="3.3" fill="none" stroke="var(--green-bright)" stroke-width=".9"/></svg>
      <span>9:00<small>am</small>-1:00<small>pm</small> <span class="and">and</span> 3:00<small>pm</small>-7:00<small>pm</small></span>
    </div>
  </div>
  <p class="address">
    <svg class="icon" width="7" height="10" viewBox="0 0 7 10" aria-hidden="true"><path d="M3.5 0A3.5 3.5 0 0 0 0 3.5C0 6 3.5 10 3.5 10S7 6 7 3.5A3.5 3.5 0 0 0 3.5 0z" fill="var(--navy-deep)"/><circle cx="3.5" cy="3.5" r="1.3" fill="var(--green)"/></svg>
    Quinta do Vale Morto Bloco 4C, loja 3, 8400-527 Lagoa
  </p>

  <p class="store-label">Online Store:</p>
  <p class="store-url">loja.bright-ledger.example</p>
  <p class="site-url">
    <svg class="icon" width="8" height="8" viewBox="0 0 8 8" aria-hidden="true"><g fill="none" stroke="var(--navy)" stroke-width=".8"><circle cx="4" cy="4" r="3.4"/><ellipse cx="4" cy="4" rx="1.5" ry="3.4"/><path d="M.6 4h6.8"/></g></svg>
    bright-ledger.example
  </p>

</main>
</body>
</html>
```